Website for a Psychologist in Private Practice

I need a cool web design for my website: www.drquorvat.com. I would like it to look professional. Keep all the current content and add: Space for video; radio spots (see Velvet Tide Hour Logo below for those); Quick Inquiry; Brindlepost link; 5 star rating on Zunq; a map; reviews from former patients. I am open to suggestions.

Target Market(s)

Those seeking individual and marital counseling.

Industry/Entity Type

Mental Health

Number of Pages Required

1 page

Font styles to use
Sans Serif
Other font styles liked:
• I'm open but no hard to read script

Requirements
Must have
• All the content on my home page with link for video and radio spots. List services and degrees and expertices (pics not necessary).
Nice to have
• A video of me and radio conversations (logo of Velvet Tide Hour radio attached).
Should not have
• Cartoons, comedy, etc.... I don't need pictures of services (marital, depression, etc...) Just list those.

```html
<!DOCTYPE html>
<html lang="en">
<head>
<meta charset="utf-8">
<title>Dr. Marla J. Quorvat — Clinical Psychologist</title>
<link rel="stylesheet" href="https://fonts.googleapis.com/css2?family=Josefin+Sans:wght@300;400;600;700&family=Open+Sans:wght@400;600;700&family=Cormorant+Garamond:wght@500&display=swap">
<style>
:root{
  --navy:#1f4d78;
  --band:#2b5f8c;
  --label:#3b87c4;
  --gold:#c8b25c;
  --sand:#d9cfbf;
  --ink:#4a4a4a;
  --muted:#8a8a8a;
  --white:#ffffff;
  --field:#ebebeb;
  --logo:#c2a84a;
}
*{box-sizing:border-box;margin:0;padding:0}
html,body{width:1200px;height:2956px;overflow:hidden}
body{position:relative;background:var(--sand);font-family:"Open Sans",Arial,sans-serif;color:var(--ink)}
.abs{position:absolute}
.backdrop{left:0;top:0;width:1200px;height:1060px;background:linear-gradient(180deg,#5fa9c4 0%,#7dbccc 40%,#a9c7c0 62%,#d6cab4 80%,var(--sand) 100%)}
.header{left:76px;top:28px;width:1048px;height:160px;background:rgba(255,255,255,.93);border-radius:4px}
.brand{left:26px;top:26px;font-family:"Josefin Sans",sans-serif;font-size:34px;font-weight:600;color:var(--logo)}
.brand small{font-size:27px;font-weight:400}
.nav{left:26px;top:94px;display:flex;gap:26px;font-size:14px;font-weight:700;color:#3d3d3d;letter-spacing:.3px}
.contact-item{top:28px;display:flex;align-items:center;gap:12px;font-size:13px;color:#555;line-height:17px}
.contact-item .icon{width:40px;height:40px;border-radius:50%;background:#e4eef7;display:flex;align-items:center;justify-content:center}
.contact-item .blue{color:var(--label);font-weight:600}
.social-top{right:24px;top:88px;display:flex;gap:8px}
.social-top span{width:24px;height:24px;border:1.5px solid #9a9a9a;border-radius:50%}
.slider{left:74px;top:184px;width:1052px;height:466px;background:var(--white);padding:12px;border-radius:4px;box-shadow:0 2px 8px rgba(0,0,0,.15)}
.slide-photo{width:100%;height:100%;background:radial-gradient(circle at 52% 40%,#ffe29a 0%,#f3a64a 22%,#b4652c 52%,#5d3622 100%)}
.slide-arrow{top:220px;width:30px;height:30px;border-radius:50%;border:2px solid #fff;background:rgba(0,0,0,.2)}
.caption{left:12px;width:1028px;text-align:center;font-family:"Cormorant Garamond",serif;color:#fff;text-shadow:0 2px 6px rgba(0,0,0,.4)}
.feature{top:684px;width:326px;height:326px;border-radius:50%;border:7px solid #dcdcdc;overflow:hidden;background:#fff}
.feature .art{width:100%;height:100%}
.feature .label{position:absolute;left:0;bottom:0;width:100%;height:74px;background:var(--label);color:#fff;font-family:"Josefin Sans",sans-serif;font-size:22px;font-weight:600;text-align:center;padding-top:14px}
.play{left:50%;top:43%;width:74px;height:74px;margin:-37px 0 0 -37px;border-radius:50%;border:4px solid #fff;background:rgba(0,0,0,.25)}
.welcome-band{left:0;top:1030px;width:1200px;height:590px;background:var(--band);clip-path:polygon(0 22px,1200px 0,1200px 530px,0 590px)}
.welcome{left:74px;top:1105px;width:1052px;color:#fff}
.welcome .pre{font-family:"Josefin Sans",sans-serif;font-size:28px;font-weight:300;line-height:28px}
.welcome h1{font-family:"Josefin Sans",sans-serif;font-size:36px;font-weight:400;letter-spacing:.5px;line-height:40px;margin-bottom:12px}
.welcome p{font-size:13px;line-height:23px;margin-bottom:14px}
.pill{left:428px;top:1657px;width:344px;height:46px;border-radius:23px;background:var(--gold);color:#fff;font-family:"Josefin Sans",sans-serif;font-weight:600;font-size:21px;text-align:center;line-height:50px}
.review{top:1774px;height:236px;background:#fff;border-radius:3px}
.review .avatar{left:50%;top:-42px;width:68px;height:68px;margin-left:-34px;border-radius:50%;border:4px solid #fff;background:linear-gradient(#b8977c,#7b5b46)}
.review .quote{font-family:"Cormorant Garamond",serif;font-size:64px;color:#ddd;line-height:1}
.review p{position:absolute;left:22px;right:22px;top:38px;text-align:center;font-size:13px;line-height:28px;color:#888}
.review .foot{left:0;bottom:0;width:100%;height:66px;background:#eee9e2;padding:16px 28px}
.review .name{font-family:"Josefin Sans",sans-serif;font-weight:600;font-size:17px;color:#333}
.review .role{font-size:12px;color:#999}
.stars{right:28px;top:28px;color:#e6a52c;font-size:16px;letter-spacing:1px}
.rule{left:74px;top:2038px;width:1052px;height:1px;background:#bfb4a4}
.rule-btn{top:2028px;width:22px;height:22px;border-radius:50%;border:1.5px solid #8d8475;background:var(--sand);font-size:11px;color:#8d8475;text-align:center;line-height:19px}
.box{left:74px;width:692px;background:#fff;border-radius:3px;text-align:center}
.expertise h2{font-family:"Josefin Sans",sans-serif;font-weight:400;font-size:25px;line-height:30px;color:var(--label);letter-spacing:1px}
.expertise .row{font-family:"Josefin Sans",sans-serif;font-size:16px;line-height:22px;color:#777}
.expertise .row i{font-style:normal;color:#bbb;padding:0 6px}
.expertise h3{font-family:"Josefin Sans",sans-serif;font-weight:400;font-size:21px;line-height:26px;color:#777;letter-spacing:.5px;margin-top:4px}
.dash{display:inline-block;width:52px;height:2px;background:var(--gold);vertical-align:middle;margin:0 10px}
.charity{font-family:"Josefin Sans",sans-serif;font-size:24px;font-weight:600;color:var(--ink);display:inline-flex;align-items:center;gap:10px;margin:0 32px}
.charity .mark{width:22px;height:22px;background:var(--muted)}
.inquiry{left:794px;top:2100px;width:332px;height:460px;background:#fff;border-radius:3px;overflow:hidden}
.inquiry .top{height:150px;background:var(--gold);text-align:center;color:#fff;padding-top:14px}
.inquiry .top .t1{font-size:16px;font-weight:600}
.inquiry .top .btn{margin:6px auto 6px;width:296px;height:38px;border-radius:19px;background:var(--label);font-family:"Josefin Sans",sans-serif;font-size:27px;line-height:42px}
.inquiry .top .t2{font-size:13px;line-height:17px;padding:0 40px}
.field{left:18px;width:296px;height:38px;background:var(--field);border-radius:3px;font-size:13px;color:#777;padding:11px 10px}
.submit{left:18px;top:398px;width:296px;height:40px;background:#7da5d3;border-radius:3px;color:#fff;font-weight:700;font-size:14px;text-align:center;line-height:40px;box-shadow:0 2px 0 #5b85b6}
.footer{left:0;top:2622px;width:1200px;height:284px;background:var(--navy);color:#fff}
.fcol{top:34px;width:246px}
.fcol h4{font-size:12.5px;font-weight:700;letter-spacing:.3px;padding-bottom:14px;border-bottom:1px solid rgba(255,255,255,.25);margin-bottom:14px}
.fcol p,.fcol li{font-size:13px;line-height:24px;list-style:none}
.finfo{display:flex;gap:12px;align-items:flex-start;margin-bottom:14px;font-size:13px;line-height:19px}
.map{left:0;top:56px;width:246px;height:162px;background:linear-gradient(135deg,#e8e4da,#d5d0c4);border-radius:2px}
.bottom{left:0;top:2906px;width:1200px;height:50px;background:var(--gold);color:#fff;font-size:13px}
.bsocial{right:74px;top:11px;display:flex;gap:20px;align-items:center}
.bsocial span{display:flex;align-items:center;gap:8px}
.bsocial i{width:26px;height:26px;border:1.5px solid #fff;border-radius:50%}
</style>
</head>
<body>

<div class="abs backdrop" role="img" aria-label="Beach scene with ocean water meeting sand"></div>

<header class="abs header">
  <div class="abs brand"><small>Dr.</small> Marla J. Quorvat</div>
  <nav class="abs nav"><span>HOME</span><span>SESSIONS</span><span>RESOURCES</span><span>BIO</span><span>CONTACT</span></nav>
  <div class="abs contact-item" style="left:554px">
    <div class="icon"><svg width="20" height="20" viewBox="0 0 20 20"><path d="M10 2 2 9h2.5v8h4v-5h3v5h4V9H18z" fill="#3b87c4"/></svg></div>
    <div>418 LARKSPUR AVENUE #120<br>HARBOR VALE, CA. 90210</div>
  </div>
  <div class="abs contact-item" style="left:818px">
    <div class="icon"><svg width="20" height="20" viewBox="0 0 20 20"><path d="M5 2h3l1.5 4-2 1.5a10 10 0 0 0 5 5l1.5-2 4 1.5v3a2 2 0 0 1-2 2A15 15 0 0 1 3 4a2 2 0 0 1 2-2z" fill="#3b87c4"/></svg></div>
    <div><span class="blue">(555) 210 4837</span><br>MQ@DRQUORVAT.COM</div>
  </div>
  <div class="abs social-top" aria-label="Social links"><span></span><span></span><span></span></div>
</header>

<section class="abs slider">
  <div class="slide-photo" role="img" aria-label="Hands framing the setting sun through a field of tall wheat"></div>
  <div class="abs slide-arrow" style="left:28px"></div>
  <div class="abs slide-arrow" style="right:28px"></div>
  <div class="abs caption" style="top:290px;font-size:32px">Lorem Ipsum Dolor Sit Amet</div>
  <div class="abs caption" style="top:322px;font-size:52px">Consectetur Adipiscing Elit</div>
</section>

<div class="abs feature" style="left:75px">
  <div class="art" role="img" aria-label="Portrait photo of the psychologist" style="background:linear-gradient(160deg,#e9d2a8,#b98f6b 55%,#3d6f9c)"></div>
  <div class="label">Dr. Marla Q</div>
</div>
<div class="abs feature" style="left:436px">
  <div class="art" role="img" aria-label="Video still of a counseling conversation" style="background:linear-gradient(160deg,#d9d4cc,#8f8a82 55%,#4f7a8c)"></div>
  <div class="abs play"><svg width="66" height="66" viewBox="0 0 66 66"><path d="M26 18 48 33 26 48z" fill="#fff"/></svg></div>
  <div class="label">Watch Our Video</div>
</div>
<div class="abs feature" style="left:798px">
  <div class="art" role="img" aria-label="Velvet Tide Hour radio show artwork with a vintage radio" style="background:radial-gradient(circle at 50% 40%,#bfe6e4,#7cc7c9 70%)"></div>
  <div class="label">Radio Spots</div>
</div>

<div class="abs welcome-band"></div>
<section class="abs welcome">
  <div class="pre">Welcome to</div>
  <h1>DR. MARLA J. QUORVAT</h1>
  <p>I'm so glad you are here. Choosing to see a professional for issues in your life can be difficult but also possibly life changing. Many postpone seeking help because they believe doing so acknowledges failure on their part. Really? We seek the help of experts all the time (contractors, mechanics, chefs, etc...) and what is more important than your life? Consulting with a neutral party to act in your best interest can be time well spent. So if you are willing to take the time to invest in counseling, make sure that it is with someone that is worth your time.</p>
  <p>Choose a licensed psychologist with a doctoral degree (Ph.D. or PsyD.) - both have over 10 years of education in the field of psychology, extensive internships and comprehensive licensing exams. Others have far less education if any. Also, consider the therapist's approach to therapy. I use a straightforward approach (psychobabble available upon request) with brief, solution-oriented sessions.</p>
  <p>Experience also separates good psychologists from others with fewer and more proficient sessions. My 20+ years of professional experience and my life experience contributes to the empathetic perspective I use to relate to each person I see. I also believe it is the reason 90% of my practice is referral based and why many other psychologists in the area seek my services.</p>
  <p><b>DO NOT COMPROMISE.</b> Find an educated, licensed, experienced professional that you can relate to. Think about what it took to get you here and the importance resolving this issue can have on your life.</p>
</section>

<div class="abs pill">REVIEWS FROM PATIENTS</div>

<div class="abs review" style="left:74px;width:330px">
  <div class="abs avatar" role="img" aria-label="Patient avatar"></div>
  <div class="abs quote" style="left:16px;top:-4px">&ldquo;</div>
  <p>Lorem ipsum dolor sit amet, consectetur adipiscing elit, sed do eiusmod tempor incididunt ut labore et dolore magna aliqua. Ut enim ad minim veniam, quis nostrud.</p>
  <div class="abs foot"><div class="name">John Doe</div><div class="role">Lorem Ipsum</div><div class="abs stars">★★★★☆</div></div>
  <div class="abs quote" style="right:12px;top:150px">&rdquo;</div>
</div>
<div class="abs review" style="left:436px;width:330px">
  <div class="abs avatar" role="img" aria-label="Patient avatar"></div>
  <div class="abs quote" style="left:16px;top:-4px">&ldquo;</div>
  <p>Lorem ipsum dolor sit amet, consectetur adipiscing elit, sed do eiusmod tempor incididunt ut labore et dolore magna aliqua. Ut enim ad minim veniam, quis nostrud.</p>
  <div class="abs foot"><div class="name">John Doe</div><div class="role">Lorem Ipsum</div><div class="abs stars">★★★★☆</div></div>
  <div class="abs quote" style="right:12px;top:150px">&rdquo;</div>
</div>
<div class="abs review" style="left:796px;width:330px">
  <div class="abs avatar" role="img" aria-label="Patient avatar"></div>
  <div class="abs quote" style="left:16px;top:-4px">&ldquo;</div>
  <p>Lorem ipsum dolor sit amet, consectetur adipiscing elit, sed do eiusmod tempor incididunt ut labore et dolore magna aliqua. Ut enim ad minim veniam, quis nostrud.</p>
  <div class="abs foot"><div class="name">John Doe</div><div class="role">Lorem Ipsum</div><div class="abs stars">★★★★☆</div></div>
  <div class="abs quote" style="right:12px;top:150px">&rdquo;</div>
</div>

<div class="abs rule"></div>
<div class="abs rule-btn" style="left:563px">&lsaquo;</div>
<div class="abs rule-btn" style="left:615px">&rsaquo;</div>

<section class="abs box expertise" style="top:2100px;height:216px;padding-top:46px">
  <h2><span class="dash"></span>EXPERTISE<span class="dash"></span></h2>
  <div class="row" style="margin-top:8px">Dating <i>•</i> Marriage <i>•</i> Parenting &amp; Professional</div>
  <h3>RELATIONSHIPS</h3>
  <div class="row" style="margin-top:10px">Depression &amp; Anxiety Issues <i>•</i> Personality Disorders <i>•</i> Life Management</div>
</section>

<section class="abs box" style="top:2346px;height:214px;padding-top:48px">
  <div style="font-family:'Josefin Sans',sans-serif;font-size:21px;color:#444">A portion of all revenue is donated to</div>
  <div style="margin-top:32px">
    <span class="charity"><span class="mark"></span>Harborlight</span>
    <span class="charity">Cedar Hearth</span>
  </div>
</section>

<section class="abs inquiry">
  <div class="top">
    <div class="t1">CONTACT US TODAY FOR YOUR</div>
    <div class="btn">QUICK INQUIRY</div>
    <div class="t2">Fill out the form below and we'll be in touch within 24 hours!</div>
  </div>
  <div class="abs field" style="top:172px">Name</div>
  <div class="abs field" style="top:220px">Email</div>
  <div class="abs field" style="top:268px">Phone</div>
  <div class="abs field" style="top:316px;height:70px">How Can we help you?</div>
  <div class="abs submit">SUBMIT</div>
</section>

<footer class="abs footer">
  <div class="abs fcol" style="left:74px">
    <h4 style="border:none;padding-bottom:0;margin-bottom:0">CLINICAL PSYCHOLOGIST</h4>
    <p style="padding-bottom:12px;border-bottom:1px solid rgba(255,255,255,.25);margin-bottom:12px">California # PSY20418</p>
    <p style="line-height:25px">Doctoral Degree in Clinical Psychology<br>Masters Degree in Counseling<br>Psychology Doctoral Internship, CVU<br>Medical Center Masters Internship,<br>Westbrook Clinic</p>
  </div>
  <div class="abs fcol" style="left:344px">
    <h4>CONTACT INFORMATION</h4>
    <div class="finfo"><svg width="16" height="20" viewBox="0 0 16 20"><path d="M8 0a7 7 0 0 0-7 7c0 5 7 13 7 13s7-8 7-13a7 7 0 0 0-7-7zm0 10a3 3 0 1 1 0-6 3 3 0 0 1 0 6z" fill="#fff"/></svg><span>418 Larkspur Avenue, Suite 120<br>Harbor Vale, CA 90210</span></div>
    <div class="finfo" style="font-size:17px"><svg width="18" height="18" viewBox="0 0 20 20"><path d="M5 2h3l1.5 4-2 1.5a10 10 0 0 0 5 5l1.5-2 4 1.5v3a2 2 0 0 1-2 2A15 15 0 0 1 3 4a2 2 0 0 1 2-2z" fill="#fff"/></svg><span>(555) 210 4837</span></div>
    <div class="finfo"><svg width="18" height="14" viewBox="0 0 18 14"><rect width="18" height="14" rx="1" fill="#fff"/><path d="M1 1l8 6 8-6" stroke="#1f4d78" stroke-width="1.5" fill="none"/></svg><span>mq@drquorvat.com</span></div>
  </div>
  <div class="abs fcol" style="left:614px">
    <h4>FIND US ON MAP</h4>
    <div class="abs map" role="img" aria-label="Street map showing the office location"></div>
  </div>
  <div class="abs fcol" style="left:884px">
    <h4>QUICK LINKS</h4>
    <ul><li>Home</li><li>Sessions</li><li>Resources</li><li>Bio</li><li>Contact</li></ul>
  </div>
</footer>

<div class="abs bottom">
  <div class="abs" style="left:74px;top:17px">©2016 Dr. Marla J. Quorvat. All Rights Reserved.</div>
  <div class="abs bsocial">
    <span><i></i>Zunq</span>
    <span><i></i>Brindlepost</span>
    <span><i></i>Chirpwell</span>
  </div>
</div>

</body>
</html>
```